Flyer Design for Upcoming Baseball Clinics, Camps, and Academies

What We Need:
We are looking for a design template we can use for our upcoming sports camps, clinics, and academies. We do elite level training with youth to professional athletes and brand awareness is our number one concern right now.

Ideally this template can be used across multiple sports. Here is our premise:

Clinics (1-Day Event to attract 50+ Athletes)
Camps (2-4 Day Events looking to attract 100+)
Academies (More intimate and skill specific. lasts 6-8 weeks. 10-20 athletes)

Our plan is to do this for Baseball, Football, Basketball, and Lacrosse.

The ideal situation is to be able to use this as a template so we can just edit the document in the future.

Target Market(s)

Prep: Middle School Athletes / ELITE: High School Athletes

Industry/Entity Type

Training

Requirements
Must have
• Things to include:
• Logo, Dates, Times, Investment, Description, Benefits, our mission statement, etc. Our specific colors, specific font family (Bunken Tech Sans Wide), follow our branding deck which is attached.
• Info:
• K7Z BASEBALL CLINIC
• Date: November 11th, 2017
• AGES: PREP: (5th to 8th Grade). ELITE (9th-12th Grade)
• Registration: 8:00am - 9:00 am / 11:00 am - Noon
• Times:
• PREP: 9:00am - 11:00 am
• ELITE: Noon - 2pm
• Investment: $199
• Current Members: $99
Nice to have
• It would be nice to see our mission statement tied in somehow in a unique way. Also maybe a testimonial or two from our pro athletes??
Should not have
• Fake Images: Any Image used needs to be real and give off an authentic feel of a baseball player and the culture.

```html
<!DOCTYPE html>
<html lang="en">
<head>
<meta charset="utf-8">
<title>K7Z Baseball Clinic Flyer</title>
<link rel="stylesheet" href="https://fonts.googleapis.com/css2?family=Michroma&family=Orbitron:wght@600;700;800&display=swap">
<style>
  :root {
    --paper: #e2e4e6;
    --paper-dark: #c9ccd0;
    --slate: #1b1f25;
    --silver-light: #f2f3f4;
    --silver-dark: #7d8187;
    --ink-light: #ffffff;
    --label: #c7c9cc;
    --ink-dark: #3a3f47;
  }
  * { margin: 0; padding: 0; box-sizing: border-box; }
  html, body { width: 927px; height: 1200px; overflow: hidden; background: var(--paper); }
  .flyer {
    position: relative; width: 927px; height: 1200px; overflow: hidden;
    background: radial-gradient(ellipse at 50% 30%, var(--silver-light), var(--paper) 60%, var(--paper-dark));
    font-family: "Orbitron", sans-serif;
  }
  .backdrop { position: absolute; inset: 0; }
  .brand-mark {
    position: absolute; left: 263px; top: 95px; width: 400px; text-align: center;
    font-family: "Michroma", sans-serif; font-size: 96px; line-height: 1; color: var(--silver-dark);
  }
  .brand-sub {
    position: absolute; left: 263px; top: 335px; width: 400px; text-align: center;
    font-family: "Michroma", sans-serif; font-size: 14px; letter-spacing: 9px; color: var(--ink-dark);
  }
  .clinic-title {
    position: absolute; left: 72px; top: 462px; width: 800px; text-align: center;
    white-space: nowrap; font-family: "Orbitron", sans-serif; font-weight: 800;
    font-size: 44px; line-height: 54px; letter-spacing: 3px; color: var(--ink-light);
    transform: rotate(-16deg); transform-origin: center;
  }
  .info { position: absolute; left: 149px; top: 652px; color: var(--ink-light); }
  .info h2 { font-size: 24px; font-weight: 700; color: var(--label); letter-spacing: 1.5px; line-height: 30px; margin-bottom: 18px; }
  .info p { font-size: 15px; font-weight: 700; line-height: 21.8px; letter-spacing: 1px; white-space: nowrap; }
  .details { position: absolute; left: 528px; top: 0; color: var(--ink-light); font-weight: 700; white-space: nowrap; }
  .detail { position: absolute; left: 0; }
  .detail h3 { font-size: 22px; font-weight: 700; color: var(--label); letter-spacing: 1.5px; line-height: 26px; }
  .detail .value-lg { font-size: 20.5px; line-height: 25px; letter-spacing: 1px; }
  .detail .value-sm { font-size: 16.5px; line-height: 24px; letter-spacing: 1px; }
  .detail .lbl { color: var(--label); }
  .d-date { top: 552px; } .d-ages { top: 616px; } .d-reg { top: 707px; } .d-times { top: 801px; }
  .seal-text {
    position: absolute; text-align: center; font-family: "Orbitron", sans-serif; font-weight: 700;
    color: var(--ink-dark); text-transform: uppercase; white-space: nowrap;
  }
  .mission { left: 47px; top: 985px; width: 240px; font-size: 13.5px; line-height: 27px; }
  .mission .seal-head { font-size: 19px; line-height: 30px; }
  .investment { left: 324px; top: 993px; width: 200px; font-size: 16px; line-height: 24px; letter-spacing: 1px; }
  .investment .price { display: block; font-size: 23px; line-height: 30px; margin-bottom: 8px; }
  .contact { position: absolute; left: 598px; top: 1038px; color: var(--ink-dark); font-weight: 700; white-space: nowrap; }
  .contact .row { font-size: 23px; line-height: 30px; letter-spacing: 1px; }
  .contact .row span { font-size: 19px; letter-spacing: 1px; }
  .social { position: absolute; left: 600px; top: 1117px; display: flex; align-items: center; gap: 13px; }
  .social .mark { width: 46px; height: 46px; background: var(--silver-dark); border-radius: 6px; }
  .social .handle { font-family: "Orbitron", sans-serif; font-weight: 700; font-size: 15px; color: var(--ink-dark); letter-spacing: 1px; }
</style>
</head>
<body>
<main class="flyer">
  <svg class="backdrop" width="927" height="1200" viewBox="0 0 927 1200">
    <defs>
      <linearGradient id="silverBar" x1="0" y1="0" x2="1" y2="1">
        <stop offset="0" stop-color="#f4f5f6"/><stop offset="0.5" stop-color="#a9adb2"/><stop offset="1" stop-color="#e9eaec"/>
      </linearGradient>
      <linearGradient id="slateFill" x1="0" y1="0" x2="1" y2="1">
        <stop offset="0" stop-color="#262b32"/><stop offset="1" stop-color="#14171c"/>
      </linearGradient>
      <radialGradient id="sealFill" cx="0.4" cy="0.35" r="0.7">
        <stop offset="0" stop-color="#f1f2f3"/><stop offset="0.6" stop-color="#bdc0c4"/><stop offset="1" stop-color="#8f9399"/>
      </radialGradient>
      <linearGradient id="leftPhoto" x1="0" y1="0" x2="0" y2="1">
        <stop offset="0" stop-color="#3f5a33"/><stop offset="0.55" stop-color="#5b8a3c"/><stop offset="0.8" stop-color="#a8694a"/><stop offset="1" stop-color="#9a5c3f"/>
      </linearGradient>
      <linearGradient id="rightPhoto" x1="0" y1="0" x2="0" y2="1">
        <stop offset="0" stop-color="#c98b62"/><stop offset="0.3" stop-color="#4f8a3a"/><stop offset="0.7" stop-color="#3f7a31"/><stop offset="1" stop-color="#c98b62"/>
      </linearGradient>
    </defs>

    <polygon class="photo-runner" role="img" aria-label="Photo of a young baseball player in a white uniform running the bases"
      points="0,0 143,0 326,440 0,548" fill="url(#leftPhoto)"/>
    <polygon class="photo-field" role="img" aria-label="Aerial photos of a pitcher and a batter on a baseball field"
      points="790,0 927,0 927,292 655,356" fill="url(#rightPhoto)"/>

    <polygon class="v-edge" points="143,0 160,0 340,436 326,440" fill="url(#silverBar)"/>
    <polygon class="v-edge" points="775,0 790,0 655,356 640,360" fill="url(#silverBar)"/>

    <polygon class="dark-band" points="0,560 927,300 927,893 0,1200" fill="url(#slateFill)"/>
    <polygon class="silver-stripe" points="0,540 927,280 927,300 0,560" fill="url(#silverBar)"/>
    <polygon class="silver-stripe" points="0,640 927,382 927,394 0,652" fill="url(#silverBar)"/>
    <polygon class="silver-stripe" points="0,1160 927,875 927,893 0,1180" fill="url(#silverBar)"/>

    <g class="seal seal-mission">
      <circle cx="167" cy="1054" r="120" fill="none" stroke="#9ea2a7" stroke-width="12" stroke-dasharray="9 6"/>
      <circle cx="167" cy="1054" r="118" fill="url(#sealFill)"/>
    </g>
    <g class="seal seal-investment">
      <circle cx="424" cy="1058" r="118" fill="none" stroke="#9ea2a7" stroke-width="12" stroke-dasharray="9 6"/>
      <circle cx="424" cy="1058" r="116" fill="url(#sealFill)"/>
    </g>
  </svg>

  <div class="brand-mark">K7Z</div>
  <div class="brand-sub">TRAINING HOUSE</div>

  <h1 class="clinic-title">K7Z BASEBALL CLINIC</h1>

  <section class="info">
    <h2>Info:</h2>
    <p>Lorem ipsum dolor sit<br>amet, consectetur<br>adipiscing elit, sed do<br>eiusmod tempor<br>incididunt ut labore et<br>dolore magna aliqua. Ut<br>enim ad minim veniam,<br>quis nostrud exercitation<br>ullamco laboris nisi ut</p>
  </section>

  <section class="details">
    <div class="detail d-date">
      <h3>Date:</h3>
      <div class="value-lg">November 11th, 2017</div>
    </div>
    <div class="detail d-ages">
      <h3>AGES:</h3>
      <div class="value-sm">PREP: (5th to 8th Grade).<br>ELITE (9th-12th Grade)</div>
    </div>
    <div class="detail d-reg">
      <h3>Registration:</h3>
      <div class="value-lg">8:00am - 9:00 am /<br>11:00 am - Noon</div>
    </div>
    <div class="detail d-times">
      <h3>Times:</h3>
      <div class="value-lg"><span class="lbl">PREP:</span> 9:00am - 11:00 am<br><span class="lbl">ELITE:</span> Noon - 2pm</div>
    </div>
  </section>

  <div class="seal-text mission">
    <div class="seal-head">Our Mission:</div>
    To train, instruct<br>motivate &amp; empower<br>the athlete<br>inside you
  </div>

  <div class="seal-text investment">
    Investment:<span class="price">$199</span>Current<br>Members:<span class="price">$99</span>
  </div>

  <section class="contact">
    <div class="row">phone <span>000-000-000</span></div>
    <div class="row">location <span>xxxxxxxxxxxxx</span></div>
  </section>

  <div class="social">
    <div class="mark"></div>
    <div class="handle">K7ZTRAININGHOUSE</div>
  </div>
</main>
</body>
</html>
```